Flyer Improve For Painting Company

Flyer Improve layout for painting company, attached.

Super Action Hero improve in flyer.

Flyer we are testing success with (entertainment) and Super Action Hero or Dog, no job photos.

Name of Super Action Hero or Dog.

Colours are up to your creativity.

Flyer size make A4, single sided flyer only.

Keep print format, set out tidy up.

Flyer make WOW to attract customers to hire our painting services.

Kind Regards

Mark

Painting

```html
<!DOCTYPE html>
<html lang="en">
<head>
<meta charset="utf-8">
<title>Truecoat Professional Painting – Flyer</title>
<link href="https://fonts.googleapis.com/css2?family=Open+Sans:ital,wght@0,400;0,600;0,700;1,700&family=Roboto+Condensed:ital,wght@0,400;0,700;1,700&family=Oswald:wght@600&family=Raleway:wght@400&display=swap" rel="stylesheet">
<style>
  :root{
    --page:#e9e7e4;
    --paper:#ffffff;
    --red:#e0202a;
    --red-dark:#b5121b;
    --navy:#1f2f8a;
    --blue:#1b6fc4;
    --blue-dark:#0d4f9c;
    --yellow:#ffe000;
    --yellow-warm:#ffc20e;
    --magenta:#c0369c;
    --grey:#6d6e70;
    --teal:#1a8fb5;
    --green:#3aa23a;
    --green-dark:#1f7a2a;
    --ink:#222;
    --hero-green:#7dbb3a;
    --coupon-blue:#2a7bc8;
  }
  *{box-sizing:border-box;margin:0;padding:0}
  html,body{width:925px;height:1200px;overflow:hidden}
  body{background:var(--page);font-family:"Open Sans",Arial,sans-serif;color:var(--ink)}
  .flyer{position:absolute;left:48px;top:12px;width:828px;height:1176px;background:var(--paper);overflow:hidden;box-shadow:0 2px 8px rgba(0,0,0,.15)}
  .abs{position:absolute}

  /* header */
  .swoosh{left:0;top:0;width:828px;height:140px}
  .web-top{left:200px;top:30px;width:330px;text-align:center;font:700 26px "Roboto Condensed",Arial,sans-serif;color:var(--yellow)}
  .hero-top{left:6px;top:76px;width:176px;height:190px;border-radius:40% 40% 30% 30%;background:radial-gradient(circle at 45% 40%,#a6d45a,var(--hero-green) 55%,#4f8c24)}
  .brand{left:182px;top:112px;width:380px}
  .brand-name{font:600 66px/1 "Open Sans",Arial,sans-serif;color:var(--navy);letter-spacing:1px}
  .brand-tag{font:400 27px/1 "Raleway",Arial,sans-serif;color:#333;letter-spacing:2px;margin-top:6px}
  .dog-splash{left:560px;top:112px;width:262px;height:212px;border-radius:30px;background:linear-gradient(135deg,#f4e9dc 0%,#d8c4a8 45%,#4fb5e6 70%,#f5d323 85%,#e6479a 100%)}

  /* benefit bars */
  .benefits{left:18px;top:264px;width:340px;list-style:none}
  .benefits li{color:#fff;font:600 13px/1.25 "Open Sans",Arial,sans-serif;padding:4px 10px;border-radius:0 14px 14px 0;margin-bottom:5px}
  .benefits li b{font-weight:700}
  .benefits .b-pro{background:var(--yellow);color:#222}
  .benefits .b-clean{background:var(--magenta)}
  .benefits .b-trust{background:var(--grey)}
  .benefits .b-resp{background:var(--teal)}
  .benefits .b-rel{background:var(--red)}

  .hero-mid{left:350px;top:393px;width:83px;height:160px;border-radius:40% 40% 20% 20%;background:linear-gradient(180deg,#a6d45a,var(--hero-green) 60%,#4f8c24)}

  /* experts */
  .experts{left:26px;top:472px;width:340px}
  .experts h2{font:700 29px/1 "Roboto Condensed",Arial,sans-serif;color:var(--navy);letter-spacing:-.3px;white-space:nowrap}
  .experts p{font:700 12.5px/1.3 "Open Sans",Arial,sans-serif;color:var(--blue-dark);margin-top:8px}
  .services{left:26px;top:566px;width:400px;display:grid;grid-template-columns:200px 200px;list-style:none}
  .services li{font:400 12px/15.2px "Open Sans",Arial,sans-serif;color:#222;padding-left:16px;position:relative;white-space:nowrap}
  .services li.wide{grid-column:span 2}
  .services li::before{content:"";position:absolute;left:0;top:2px;width:11px;height:11px;border-radius:50%;background:var(--red)}
  .services li::after{content:"";position:absolute;left:3.5px;top:4px;width:3px;height:5px;border:solid #fff;border-width:0 1.6px 1.6px 0;transform:rotate(45deg)}

  /* green boxes */
  .features{left:26px;top:843px;width:186px;list-style:none}
  .features li{background:linear-gradient(180deg,#4dbb47,var(--green-dark));color:#fff;font:700 12px/1.2 "Open Sans",Arial,sans-serif;padding:4px 9px;border-radius:5px;margin-bottom:3px;border:1px solid #fff;box-shadow:0 0 0 1px var(--green)}
  .towns{left:223px;top:843px;width:169px;height:136px;background:linear-gradient(180deg,#2f9a35,#16661f);border-radius:6px;border:2px solid #fff;box-shadow:0 0 0 1px var(--green);text-align:center;padding-top:6px;list-style:none}
  .towns li{font:700 18px/24.5px "Roboto Condensed",Arial,sans-serif;color:var(--yellow)}

  /* right blue + red panel */
  .promise{left:415px;top:324px;width:380px;height:104px;border-radius:14px 14px 0 0;background:linear-gradient(180deg,#3b8fe0,var(--blue-dark));text-align:center;color:#fff;padding-top:8px}
  .promise em{font:italic 700 16px/1 "Open Sans",Arial,sans-serif;display:block}
  .promise strong{font:700 28px/1.12 "Roboto Condensed",Arial,sans-serif;display:block;margin-top:4px}
  .panel{left:426px;top:428px;width:356px;height:540px;background:linear-gradient(180deg,var(--red),var(--red-dark))}
  .perks{left:440px;top:448px;width:290px;list-style:none}
  .perks li{color:#fff;font:700 14.5px/1.25 "Roboto Condensed",Arial,sans-serif;padding-left:20px;position:relative;margin-bottom:6px}
  .perks li::before{content:"";position:absolute;left:0;top:2px;width:13px;height:13px;border-radius:50%;background:#fff}
  .perks li::after{content:"";position:absolute;left:4.5px;top:4px;width:3.5px;height:6px;border:solid var(--red);border-width:0 2px 2px 0;transform:rotate(45deg)}
  .cartoon-dog{left:705px;top:576px;width:98px;height:102px;border-radius:50%;background:radial-gradient(circle at 50% 45%,#f3d3a4,#d59a52 70%,#a86a2c)}
  .book-banner{left:412px;top:663px;width:378px;height:70px;background:linear-gradient(180deg,#fff04a,var(--yellow-warm));clip-path:polygon(0 0,92% 0,100% 50%,92% 100%,0 100%);padding:7px 0 0 16px;font:700 22px/1.1 "Roboto Condensed",Arial,sans-serif;color:var(--red-dark)}
  .call{left:426px;top:744px;width:356px;text-align:center}
  .call .label{font:700 29px/1 "Roboto Condensed",Arial,sans-serif;color:var(--yellow)}
  .call .phone{font:600 52px/1 "Oswald",Arial,sans-serif;color:#fff;margin-top:6px;letter-spacing:1px}
  .call .online{font:italic 700 20px/1 "Roboto Condensed",Arial,sans-serif;color:#fff;margin-top:22px}
  .call .web{font:700 24px/1 "Roboto Condensed",Arial,sans-serif;color:var(--yellow);margin-top:8px}
  .voucher{left:432px;top:914px;width:344px;height:70px;background:linear-gradient(180deg,#3d95e6,var(--blue-dark));border-radius:40px 40px 4px 4px;text-align:center;color:#fff;padding-top:7px}
  .voucher .v1{font:700 17px/1.1 "Roboto Condensed",Arial,sans-serif}
  .voucher .v2{font:700 14px/1.2 "Roboto Condensed",Arial,sans-serif}
  .voucher .v3{font:400 12px/1.2 "Open Sans",Arial,sans-serif}

  /* contact strip + coupon */
  .strip{left:0;top:991px;width:828px;height:21px;background:var(--red);color:#fff;font:700 10.5px/21px "Open Sans",Arial,sans-serif;padding-left:20px;white-space:nowrap}
  .strip span{color:var(--yellow)}
  .coupon{left:10px;top:1013px;width:808px;height:140px;border:2px dashed var(--coupon-blue);background:#f4f9ff}
  .coupon-tab{left:24px;top:1021px;width:150px;height:24px;background:var(--red);border-radius:12px 12px 0 0;color:#fff;font:italic 700 15px/24px "Roboto Condensed",Arial,sans-serif;text-align:center}
  .coupon-tab small{font-size:12px}
  .box{display:inline-block;width:10px;height:10px;border:1px solid #444;background:#fff;vertical-align:-1px;margin-right:4px}
  .yes{left:192px;top:1034px;font:400 11px "Open Sans",Arial,sans-serif;color:var(--red)}
  .yes small{font-size:9px;color:#222}
  .jobs{left:30px;top:1053px;width:520px;font:400 11px "Open Sans",Arial,sans-serif;border-bottom:1px dotted #888;padding-bottom:1px}
  .jobtype{left:569px;top:1029px;width:236px;height:44px;border:2px solid var(--red);background:#fff;display:grid;grid-template-columns:1fr 1fr;padding:3px 8px;font:400 11px/17px "Open Sans",Arial,sans-serif}
  .mail{left:18px;top:1075px;width:336px;height:22px;background:var(--red);border-radius:0 11px 11px 0;color:#fff;font:700 10px/22px "Open Sans",Arial,sans-serif;padding-left:12px;white-space:nowrap}
  .visit{left:364px;top:1080px;font:400 11px "Open Sans",Arial,sans-serif}
  .visit span{color:var(--red)}
  .fields{left:30px;width:780px;font:400 11px "Open Sans",Arial,sans-serif;display:grid;gap:10px}
  .fields div{border-bottom:1px dotted #888}
  .row1{top:1108px;grid-template-columns:330px 200px 100px 1fr}
  .row2{top:1128px;grid-template-columns:330px 1fr}
  .bottom-band{left:0;top:1155px;width:828px;height:21px;background:linear-gradient(180deg,var(--coupon-blue),var(--blue-dark));color:#fff;font:700 10px/21px "Open Sans",Arial,sans-serif;padding-left:22px;white-space:nowrap}
</style>
</head>
<body>
<main class="flyer">
  <svg class="abs swoosh" viewBox="0 0 828 140" aria-hidden="true">
    <path d="M180 0H828V72C720 118 560 84 420 94C330 101 260 112 220 74C200 54 190 24 180 0Z" fill="#e0202a"/>
    <path d="M190 0H828V40C720 78 560 50 420 62C330 70 262 76 232 48C214 32 200 14 190 0Z" fill="#ef3a33"/>
    <path d="M420 94C560 84 720 118 828 72V82C720 126 560 94 420 104Z" fill="#9f0f16"/>
  </svg>
  <div class="abs web-top">www.truecoatpainters.com.au</div>

  <div class="abs hero-top" role="img" aria-label="Cartoon super action hero mascot in green costume and cape, flying"></div>
  <div class="abs brand">
    <div class="brand-name">TRUECOAT</div>
    <div class="brand-tag">PROFESSIONAL PAINTING</div>
  </div>
  <div class="abs dog-splash" role="img" aria-label="Bulldog puppy leaping through colourful paint splashes"></div>

  <ul class="abs benefits">
    <li class="b-pro"><b>PROFESSIONAL:</b> Highly-experienced painters</li>
    <li class="b-clean"><b>CLEAN:</b> No mess! We respect your property and clean-up after ourselves</li>
    <li class="b-trust"><b>TRUSTWORTHY:</b> We are there until we see the smile on your face!</li>
    <li class="b-resp"><b>RESPONSIBLE:</b> “Set us and forget us”</li>
    <li class="b-rel"><b>RELIABLE:</b> On time, or we will pay you $100 for each day we’re late</li>
  </ul>

  <div class="abs hero-mid" role="img" aria-label="Super action hero mascot peeking from behind the panel"></div>

  <section class="abs experts">
    <h2>LEAVE IT TO THE EXPERTS!</h2>
    <p>Avoid the stress of doing it yourself, not to mention the paint splatters, the mistakes &amp; the aches &amp; pains</p>
  </section>
  <ul class="abs services">
    <li>Residential</li><li>Internal and external</li>
    <li>Colour consultation</li><li>Body corporates, units, flats</li>
    <li>Commercial</li><li>Real estate</li>
    <li>Retail, shops, malls, hospitality</li><li>Shopping centres</li>
    <li>High rise, multi-stories</li><li>Health, Hospitals</li>
    <li>Emergency work</li><li>Aged care</li>
    <li>Hotels</li><li>Motels</li>
    <li>Retirement living</li><li>Government and Councils</li>
    <li class="wide">Education, Schools, Universities, Colleges</li>
    <li>Sports facilities</li><li>Stadiums</li>
    <li>Churches</li><li>Decorative finishes</li>
    <li>Wallpaper hanging</li><li>Anti-graffiti</li>
    <li>Line marking</li><li>Building Repairs</li>
    <li>After hour / shut downs</li><li>Factories</li>
    <li>Manufacturing</li><li>Waterproof membranes</li>
    <li>Bridges</li><li>Industrial coatings</li>
    <li>Textured coatings</li><li>Insurance work</li>
    <li class="wide">Painting maintenance programs</li>
  </ul>

  <ul class="abs features">
    <li>Residential Interior &amp;<br>Exterior Painting</li>
    <li>Commercial Painting</li>
    <li>Fully Insured &amp; Registered</li>
    <li>100% Satisfaction<br>Guarantee</li>
  </ul>
  <ul class="abs towns">
    <li>WARRNAMBOOL</li><li>COLAC</li><li>PORT FAIRY</li><li>HAMILTON</li><li>PORTLAND</li>
  </ul>

  <div class="abs promise">
    <em>We deliver peace of mind with superior:</em>
    <strong>Workmanship, Finishes<br>and Service</strong>
  </div>
  <div class="abs panel"></div>
  <ul class="abs perks">
    <li>PAINTER AND HANDYMAN</li>
    <li>SPECIALIST IN ALL RESIDENTIAL WORK</li>
    <li>PROFESSIONAL INTERIOR &amp; EXTERIOR</li>
    <li>WORRY FREE, RESIDENTIAL &amp;<br>COMMERCIAL PAINTERS</li>
    <li>RELIABLE AND AFFORDABLE,<br>EFFICIENT PAINTERS</li>
    <li>RISK FREE, SAVE TIME &amp; MONEY</li>
    <li>UNBEATEN QUALITY BEST PRICES</li>
  </ul>
  <div class="abs cartoon-dog" role="img" aria-label="Cartoon puppy holding a paintbrush"></div>
  <div class="abs book-banner">BOOK YOUR JOB TODAY,<br>LIMITED SALE TIME! HURRY!</div>
  <div class="abs call">
    <div class="label">CALL US TODAY</div>
    <div class="phone">0491 570 156</div>
    <div class="online">BOOK ONLINE NOW AT:</div>
    <div class="web">www.truecoatpainters.com.au</div>
  </div>
  <div class="abs voucher">
    <div class="v1">$100 FREE Gift Voucher off your job</div>
    <div class="v2">Download at: www.truecoatpainters.com.au</div>
    <div class="v3">One only per customer</div>
  </div>

  <div class="abs strip">COUNTRY WIDE SERVICE: <span>Truecoat Professional Painting,</span> &nbsp; Free call today 1800 160 401, &nbsp; Fax: 03 5550 1234, &nbsp; email: paint@truecoatpainters.com.au</div>

  <div class="abs coupon"></div>
  <div class="abs coupon-tab">FREE <small>EASY COUPON</small></div>
  <div class="abs yes"><span class="box"></span>YES please visit and give us a quote <small>(Valued at $147)</small> Yours FREE!</div>
  <div class="abs jobs">Jobs I want done are..........</div>
  <div class="abs jobtype">
    <span><span class="box"></span>Internal painting</span>
    <span><span class="box"></span>External painting</span>
    <span><span class="box"></span>Handyman</span>
    <span><span class="box"></span>Building</span>
  </div>
  <div class="abs mail">Mail coupon to: Truecoat PO Box 412 Warrnambool Vic 3280</div>
  <div class="abs visit">Visit time best preferred <span>time</span> ............<span>day</span>.....................<span>month</span>......................2013</div>
  <div class="abs fields row1"><div>Name:</div><div>Suburb:</div><div>P/Code:</div><div>Phone:</div></div>
  <div class="abs fields row2"><div>Address:</div><div>Email:</div></div>
  <div class="abs bottom-band">Want to talk Free 24 hours leave a message call now on 1800 160 401. &nbsp; Email or Fax FREE EASY COUPON to: paint@truecoatpainters.com.au &nbsp; Fax 03 5550 1234</div>
</main>
</body>
</html>
```